Small Machinery Hire Company Needs Coaster Design

Please design an eye catching coaster/sticker to place in local pubs and restaurants. Please use our attached logo and incorporate our rustic earthy feel into the colours. Use the following details. Definite want the focus to be on the logo and phone number.

Would appreciate if it could be multi-purpose as a basic sign as well.

Dry/Wet Hire Available
Ph: 0471629058

(Use FaceBook icon) facebook.com/bramwellkestrelplant2917/

Target Market(s)

At homer DIY-ers. Middle class men who would like to hire a machine to work on their own pride and joy home.

Industry/Entity Type

Construction Company

Font styles to use
Other font styles liked:
• Something that matches the Logo

Colors
fefdec
ec1f27
474747
919191

Requirements
Nice to have
• Preferably a square shape so the it is more multi purpose

```html
<!DOCTYPE html>
<html lang="en">
<head>
<meta charset="UTF-8">
<title>Bramwell Kestrel Plant – Sticker</title>
<link rel="stylesheet" href="https://fonts.googleapis.com/css2?family=Anton&display=swap">
<style>
  :root{
    --backdrop:#3a3a3a;
    --sand-light:#f3e3a6;
    --sand-mid:#d9bf78;
    --sand-deep:#a98a4a;
    --brand-red:#7c1a14;
    --ink:#1c1a14;
    --bucket:#161512;
    --bucket-edge:#2c2a24;
    --cream:#f2dc8c;
    --photo-dark:#2a2618;
    --photo-mid:#5e5232;
  }
  *{box-sizing:border-box;margin:0;padding:0}
  html,body{width:1200px;height:794px;overflow:hidden}
  body{
    background:var(--backdrop);
    display:flex;align-items:center;justify-content:center;
    font-family:"Anton",Impact,sans-serif;
  }
  .sticker{
    position:relative;width:900px;height:640px;overflow:hidden;
    background:linear-gradient(135deg,var(--sand-light) 0%,var(--sand-mid) 55%,var(--sand-deep) 100%);
  }
  .texture{
    position:absolute;inset:0;
    background:radial-gradient(ellipse at 25% 75%,rgba(169,138,74,.35),transparent 60%),
               radial-gradient(ellipse at 15% 20%,rgba(255,245,200,.4),transparent 55%);
  }
  .brand{
    position:absolute;left:50px;top:60px;
    color:var(--brand-red);line-height:1;
  }
  .brand-initials{display:block;font-size:190px;letter-spacing:4px}
  .brand-name{display:block;font-size:40px;letter-spacing:3px;margin-top:6px;color:var(--brand-red)}
  .machine-photo{
    position:absolute;right:0;top:0;width:440px;height:640px;
    background:linear-gradient(200deg,var(--photo-mid) 0%,var(--photo-dark) 70%,var(--sand-deep) 100%);
    clip-path:polygon(18% 0,100% 0,100% 100%,0 100%,6% 40%);
  }
  .bucket{
    position:absolute;left:330px;bottom:40px;width:520px;height:190px;
    background:var(--bucket);border:6px solid var(--bucket-edge);
    transform:rotate(-14deg);
    display:flex;flex-direction:column;align-items:center;justify-content:center;
    color:var(--cream);text-align:center;
  }
  .hire-line{font-size:40px;letter-spacing:2px}
  .phone-line{font-size:44px;letter-spacing:2px;margin-top:4px}
</style>
</head>
<body>
  <div class="sticker">
    <div class="texture"></div>
    <div class="machine-photo" role="img" aria-label="Photo of a mini loader with bucket attachment"></div>
    <div class="brand">
      <span class="brand-initials">BKP</span>
      <span class="brand-name">BRAMWELL KESTREL PLANT</span>
    </div>
    <div class="bucket">
      <p class="hire-line">Dry/Wet Hire Available</p>
      <p class="phone-line">Ph: 0471629058</p>
    </div>
  </div>
</body>
</html>
```